VRX Putt 2016 - national wide golf tournament

We organize a national golf tournament for the Young Civic Forum Switzerland (see http://www.vrx-lorvo.ch for further information).
The tournament is every year but 2016 it is our goal to organize the best golf tournament ever in a very exclusive environment (Golfclub Tannweide, http://www.tannweide.ch/wp/). There will be about 80 golfers and 150 guests in the evening. The tournament 2015 uses this website: http://www.vrxputt.ch.

We need a completely new web design to organize our event in 2016. The website should inform about all event details and enable a online self registration. We have a logo for the event and the colors should be reused. We would like to see designs with the logo colors. The main page should be a simple one page-layout with different layout blocks directly accessible via top sticky menubar:
- Home (welcome page)
- Program
- Information
- Registration (formular on homepage)
- Sponsors
- Contact

Important: On the welcome page there should be enough place for:
1. Our Golf event logo
2. Our VRX Switzerland logo
3. The Golfclub logo
4. The main sponsors logos (see VRXS_Sponsors_Section.png and http://www2.vrx.ch as input, not necessary to design it the same way)

The website will be in German in the first place but we need it multilingual.

Please see attachment for logos and pictures.
The web site will be implemented on WordPress - this is not part of this PixelHive project.

Target Market(s)

VRX Members Switzerland, Golfers in Switzerland

Number of Pages Required

3 page

Font styles to use
Sans Serif

Colors
9bcb3c
abd037
cadf82
eaf2ce
f6faec
ffffff
ecf7fb
cee9f5
85cae6

Requirements
Must have
• - multilingual (DE / FR)
• - one page layout design for main site / welcome site
• - page layout for big picture less text
• - page layout for multiple smaller pictures and multiple text blocks
• - bright design including the colors of the VRX Putt 2016 logo (greens)
• - space for pictures of the golf club / golf playeres / other
• - main sponsors logos on the front page
• - mobile version / responsive design
Nice to have
• - sponsor section => what idea do you have?
• - slider with picture on mainpage => as on vrx-lorvo.ch

```html
<!DOCTYPE html>
<html lang="en">
<head>
<meta charset="utf-8">
<title>VRX Putt 2016</title>
<link href="https://fonts.googleapis.com/css2?family=Open+Sans:wght@400;600;700&family=Raleway:wght@400;600;700;800&display=swap" rel="stylesheet">
<style>
:root{
  --green:#9bcb3c;
  --green-2:#abd037;
  --green-3:#cadf82;
  --green-4:#eaf2ce;
  --green-5:#f6faec;
  --white:#ffffff;
  --blue-1:#ecf7fb;
  --blue-2:#cee9f5;
  --blue:#85cae6;
  --ink:#333333;
  --muted:#777777;
  --line:#dddddd;
  --dark:#1f3316;
  --grey-bg:#f1f1f1;
}
*{box-sizing:border-box;margin:0;padding:0}
html,body{width:1200px;height:5000px;overflow:hidden}
body{font-family:"Open Sans",Arial,sans-serif;color:var(--ink);background:var(--white);position:relative}
.abs{position:absolute}
.heading{font-family:"Raleway",Arial,sans-serif}

/* header */
.site-header{position:absolute;top:0;left:0;width:1200px;height:120px;background:rgba(255,255,255,.96);z-index:5}
.brand{position:absolute;left:80px;top:28px;display:flex;align-items:center;gap:12px}
.brand-dot{width:54px;height:54px;border-radius:50%;background:var(--green)}
.brand-name{font-family:"Raleway",sans-serif;font-weight:700;font-size:24px;color:var(--green)}
.main-nav{position:absolute;right:80px;top:74px;display:flex;gap:36px;font-family:"Raleway",sans-serif;font-size:15px;font-weight:600;text-transform:uppercase;color:var(--ink)}
.main-nav .active{color:var(--green);border-bottom:3px solid var(--green);padding-bottom:6px}
.lang{position:absolute;right:80px;top:18px;font-size:13px;color:var(--muted)}

/* hero */
.hero{position:absolute;top:0;left:0;width:1200px;height:680px;background:linear-gradient(180deg,#cfe3ec 0%,#a9c9a0 38%,#6e9a46 62%,#4f7d2f 100%)}
.slider-arrow{position:absolute;top:390px;width:44px;height:44px;border-radius:50%;background:rgba(255,255,255,.75);display:flex;align-items:center;justify-content:center}
.welcome-card{position:absolute;left:80px;top:745px;width:780px;height:360px;background:var(--white);padding:36px 40px;box-shadow:0 4px 18px rgba(0,0,0,.12);z-index:2}
.welcome-card .pre{font-family:"Raleway",sans-serif;font-size:15px;font-weight:600;color:var(--green);text-transform:uppercase}
.welcome-card h1{font-family:"Raleway",sans-serif;font-size:34px;font-weight:800;color:var(--green);text-transform:uppercase;margin:2px 0 16px}
.welcome-card p{font-size:13px;line-height:22px;color:var(--muted);width:460px;margin-bottom:12px}
.btn-outline{display:inline-block;border:1px solid var(--green);color:var(--green);font-size:12px;padding:8px 18px;text-transform:uppercase;font-weight:600}
.circle-photo{position:absolute;left:775px;top:575px;width:340px;height:340px;border-radius:50%;border:14px solid var(--green);background:linear-gradient(160deg,#8fb4d0 0%,#b98a3a 40%,#5d8f36 80%);z-index:3}

/* section headings */
.sec-title{position:absolute;left:0;width:1200px;text-align:center}
.sec-title .small{font-family:"Raleway",sans-serif;font-size:15px;color:var(--green);text-transform:uppercase;font-weight:600}
.sec-title .big{font-family:"Raleway",sans-serif;font-size:34px;font-weight:700;color:var(--ink);text-transform:uppercase;display:inline-flex;align-items:center;gap:18px}
.sec-title .big::before,.sec-title .big::after{content:"";width:110px;height:1px;background:var(--green)}

/* program */
.program{position:absolute;top:1145px;left:0;width:1200px;height:540px;background:linear-gradient(180deg,#2c4220 0%,#1b2c12 100%)}
.program .sec-title .big{color:var(--white)}
.program-card{position:absolute;top:135px;width:262px;height:380px;background:var(--white)}
.program-card .photo{height:165px;background:linear-gradient(180deg,#bcd8ea 0%,#8ab95a 55%,#5f8d36 100%)}
.program-card h3{font-family:"Raleway",sans-serif;font-size:17px;font-weight:800;margin:16px 18px 10px}
.program-card ul{list-style:none;margin:0 18px}
.program-card li{font-size:12px;line-height:18px;color:var(--muted);padding:4px 0 4px 18px;position:relative;border-bottom:1px solid #eee}
.program-card li::before{content:"";position:absolute;left:0;top:10px;width:8px;height:8px;border-radius:50%;background:var(--green)}
.program .slider-arrow{top:305px;background:rgba(255,255,255,.15);border:1px solid rgba(255,255,255,.7)}

/* information */
.information{position:absolute;top:1690px;left:0;width:1200px;height:620px;background:var(--white)}
.info-photo{position:absolute;left:75px;top:125px;width:510px;height:345px;background:linear-gradient(180deg,#cfe1ea 0%,#8fb86a 45%,#66933b 100%)}
.info-text{position:absolute;left:615px;top:125px;width:510px}
.info-text h3{font-family:"Raleway",sans-serif;font-size:22px;font-weight:700}
.info-text .date{font-size:12px;color:var(--muted);margin:4px 0 14px}
.info-text p{font-size:13px;line-height:22px;color:var(--muted);margin-bottom:22px}

/* registration */
.registration{position:absolute;top:2310px;left:0;width:1200px;height:780px;background:linear-gradient(90deg,#5d92a8 0%,#8cbfd4 30%,#9ac7a0 60%,#6e9c45 100%)}
.reg-panel{position:absolute;left:563px;top:2230px;width:562px;height:840px;background:var(--white);box-shadow:0 4px 18px rgba(0,0,0,.15);z-index:2}
.reg-head{height:90px;background:var(--blue);padding:18px 28px;color:var(--white);position:relative}
.reg-head .small{font-family:"Raleway",sans-serif;font-size:15px;font-weight:600;text-transform:uppercase}
.reg-head .big{font-family:"Raleway",sans-serif;font-size:30px;font-weight:800;text-transform:uppercase;line-height:1}
.reg-head svg{position:absolute;right:24px;top:16px}
.reg-body{padding:16px 28px}
.reg-label{font-family:"Raleway",sans-serif;font-size:13px;font-weight:700;text-transform:uppercase;margin-bottom:4px}
.reg-hint{font-size:12px;color:var(--muted);margin-bottom:6px}
.select{height:30px;border:1px solid var(--line);font-size:12px;color:var(--muted);padding:6px 10px;margin-bottom:16px;position:relative}
.select::after{content:"";position:absolute;right:12px;top:12px;border:5px solid transparent;border-top-color:#666}
.field{display:flex;align-items:center;margin-bottom:11px}
.field label{width:150px;font-size:12px;color:var(--ink)}
.field .input{flex:1;height:30px;border:1px solid var(--line);background:var(--white);font-size:12px;color:var(--muted);padding:6px 10px;position:relative}
.field .input.select-in::after{content:"";position:absolute;right:12px;top:12px;border:5px solid transparent;border-top-color:#666}
.terms{display:flex;align-items:center;gap:10px;font-size:12px}
.check{width:14px;height:14px;border:1px solid #999}
.terms b{color:var(--green)}
.pay{display:flex;gap:6px;margin-left:auto}
.pay span{width:34px;height:20px;background:#e3e3e3;border-radius:3px}
.btn-green{display:block;margin:18px 0 0 150px;width:330px;height:44px;line-height:44px;text-align:center;background:var(--green);color:var(--white);font-family:"Raleway",sans-serif;font-weight:700;font-size:14px;text-transform:uppercase}

/* directors */
.directors{position:absolute;top:3090px;left:0;width:1200px;height:510px;background:var(--grey-bg)}
.director{position:absolute;top:140px;width:178px}
.director .photo{height:260px;background:linear-gradient(180deg,#d9dde0 0%,#9aa3aa 60%,#4b5560 100%)}
.director .name{text-align:center;font-size:12px;font-weight:600;margin-top:14px;text-transform:uppercase}
.director .role{text-align:center;font-size:11px;color:var(--muted)}

/* sponsors */
.sponsors{position:absolute;top:3600px;left:0;width:1200px;height:800px;background:var(--white)}
.tier{position:absolute;left:0;width:1200px;text-align:center}
.tier .small{font-family:"Raleway",sans-serif;font-size:12px;color:var(--muted);text-transform:uppercase}
.tier .big{font-family:"Raleway",sans-serif;font-size:24px;font-weight:700;color:var(--green);text-transform:uppercase;display:inline-flex;align-items:center;gap:16px}
.tier .big::before,.tier .big::after{content:"";width:80px;height:1px;background:var(--green-3)}
.logo-row{position:absolute;left:90px;width:1020px;display:flex;justify-content:space-between}
.sponsor{width:180px;height:56px;display:flex;align-items:center;justify-content:center;gap:8px;font-family:"Open Sans",sans-serif;font-weight:700;font-size:18px;color:#4a6b8a}
.sponsor i{width:14px;height:14px;border-radius:50%;background:var(--green);display:block}

/* footer */
.site-footer{position:absolute;top:4395px;left:0;width:1200px;height:605px;background:linear-gradient(180deg,#587f31 0%,#2f4a1a 60%,#1e3110 100%);color:var(--white)}
.footer-photo{position:absolute;left:0;top:0;width:560px;height:605px;background:radial-gradient(circle at 40% 70%,rgba(255,255,255,.35) 0%,rgba(255,255,255,0) 45%)}
.f-col{position:absolute;font-size:13px;line-height:22px;color:#e6eedc}
.f-col h4{font-family:"Raleway",sans-serif;font-size:16px;font-weight:700;color:var(--white);margin-bottom:8px}
.f-row{display:flex;align-items:center;gap:8px}
.social{display:flex;gap:8px;margin-top:6px}
.social span{width:28px;height:28px;border-radius:50%;background:rgba(255,255,255,.85)}
.copyright{position:absolute;left:0;bottom:18px;width:1200px;text-align:center;font-size:12px;color:#cfdcbf}
</style>
</head>
<body>

<section class="hero" role="img" aria-label="Photo of the golf clubhouse with green lawns and trees"></section>

<header class="site-header">
  <div class="brand"><span class="brand-dot"></span><span class="brand-name">VRX Putt 2016</span></div>
  <div class="lang">DE / FR</div>
  <nav class="main-nav">
    <span class="active">Welcome</span><span>Program</span><span>Information</span><span>Registration</span><span>Sponsors</span><span>Contact</span>
  </nav>
</header>

<div class="slider-arrow" style="left:70px"><svg width="14" height="14" viewBox="0 0 14 14"><path d="M9 2 4 7l5 5" fill="none" stroke="#333" stroke-width="2"/></svg></div>
<div class="slider-arrow" style="left:1086px"><svg width="14" height="14" viewBox="0 0 14 14"><path d="M5 2l5 5-5 5" fill="none" stroke="#333" stroke-width="2"/></svg></div>

<article class="welcome-card">
  <div class="pre">Welcome to</div>
  <h1>VRX Putt 2016</h1>
  <p>Our annual national tournament brings golfers and guests together for a full day on a beautiful course, followed by an evening dinner with friends, partners and members from all over the country.</p>
  <p>Join us for friendly competition, great food and a relaxed atmosphere. Register online below and secure your place for this exclusive day at the club.</p>
  <span class="btn-outline">Read more</span>
</article>
<div class="circle-photo" role="img" aria-label="Round photo of a pond with a fountain and autumn trees"></div>

<section class="program">
  <div class="sec-title" style="top:48px"><div class="small">Our</div><div class="big">Program</div></div>
  <div class="slider-arrow" style="left:82px"><svg width="14" height="14" viewBox="0 0 14 14"><path d="M9 2 4 7l5 5" fill="none" stroke="#fff" stroke-width="2"/></svg></div>
  <div class="slider-arrow" style="left:1074px"><svg width="14" height="14" viewBox="0 0 14 14"><path d="M5 2l5 5-5 5" fill="none" stroke="#fff" stroke-width="2"/></svg></div>
  <div class="program-card" style="left:160px">
    <div class="photo" role="img" aria-label="Golfers walking on the fairway"></div>
    <h3>FRIDAY</h3>
    <ul><li>Arrival and registration of players</li><li>Shotgun start on all holes</li><li>Lunch break at the halfway house</li><li>Dinner at the hotel terrace</li></ul>
  </div>
  <div class="program-card" style="left:470px">
    <div class="photo" role="img" aria-label="Golfer teeing off on a sunny day"></div>
    <h3>FRIDAY</h3>
    <ul><li>Arrival and registration of players</li><li>Shotgun start on all holes</li><li>Lunch break at the halfway house</li><li>Dinner at the hotel terrace</li></ul>
  </div>
  <div class="program-card" style="left:780px">
    <div class="photo" role="img" aria-label="Golf ball near the hole on the green"></div>
    <h3>FRIDAY</h3>
    <ul><li>Arrival and registration of players</li><li>Shotgun start on all holes</li><li>Lunch break at the halfway house</li><li>Dinner at the hotel terrace</li></ul>
  </div>
</section>

<section class="information">
  <div class="sec-title" style="top:40px"><div class="small">About our</div><div class="big">Information</div></div>
  <div class="info-photo" role="img" aria-label="Golf course with bunkers and trees"></div>
  <div class="info-text">
    <h3>Lorem Ipsum dolor sit amet</h3>
    <div class="date">12 March 2016</div>
    <p>All details about the tournament day are collected here: the course, the format of play, the prizes and the evening programme. Players receive their start times by email one week before the event, and guests for dinner are welcome from six in the evening.</p>
    <p>Parking is available directly at the clubhouse. For questions about handicaps, rental equipment or hotel rooms near the club, please contact the organising team at any time.</p>
    <span class="btn-outline">Read more</span>
  </div>
</section>

<section class="registration" role="img" aria-label="Photo of a golfer in a cap finishing his swing"></section>

<form class="reg-panel">
  <div class="reg-head">
    <div class="small">Online</div><div class="big">Registration</div>
    <svg width="46" height="46" viewBox="0 0 46 46"><rect x="3" y="8" width="32" height="34" fill="none" stroke="#fff" stroke-width="2.5"/><path d="M20 28 38 6l5 5-18 22-7 2z" fill="none" stroke="#fff" stroke-width="2.5"/></svg>
  </div>
  <div class="reg-body">
    <div class="reg-label">Registration option</div>
    <div class="reg-hint">Please select the option you want for the registration</div>
    <div class="select">1 x golfer incl. dinner and greenfee (CHF 180.00)</div>
    <div class="reg-label" style="margin-bottom:12px">Personal information 1</div>
    <div class="field"><label>Lose *</label><div class="input select-in">Please</div></div>
    <div class="field"><label>Name *</label><div class="input"></div></div>
    <div class="field"><label>First Name *</label><div class="input"></div></div>
    <div class="field"><label>Street House Number *</label><div class="input"></div></div>
    <div class="field"><label>ZIP City *</label><div class="input"></div></div>
    <div class="field"><label>E-Mail Address *</label><div class="input"></div></div>
    <div class="field"><label>Mobile *</label><div class="input"></div></div>
    <div class="field"><label>Home Club *</label><div class="input select-in">Please</div></div>
    <div class="field"><label>Handicap *</label><div class="input"></div></div>
    <div class="field"><label>ASG number *</label><div class="input"></div></div>
    <div class="field"><label>Terms *</label>
      <div class="terms"><span class="check"></span>I have the <b>[Conditions]</b> read and accept</div>
      <div class="pay"><span></span><span></span></div>
    </div>
    <span class="btn-green">Next to the price overview</span>
  </div>
</form>

<section class="directors">
  <div class="sec-title" style="top:40px"><div class="small">Board of</div><div class="big">Directors</div></div>
  <div class="director" style="left:92px"><div class="photo" role="img" aria-label="Portrait of a board member in a suit"></div><div class="name">Lukas Brenner</div><div class="role">President</div></div>
  <div class="director" style="left:301px"><div class="photo" role="img" aria-label="Portrait of a board member in a suit"></div><div class="name">Lukas Brenner</div><div class="role">Vice President</div></div>
  <div class="director" style="left:511px"><div class="photo" role="img" aria-label="Portrait of a board member in a suit"></div><div class="name">Lukas Brenner</div><div class="role">Finance</div></div>
  <div class="director" style="left:720px"><div class="photo" role="img" aria-label="Portrait of a board member in a suit"></div><div class="name">Lukas Brenner</div><div class="role">Sponsoring</div></div>
  <div class="director" style="left:930px"><div class="photo" role="img" aria-label="Portrait of a board member in a suit"></div><div class="name">Lukas Brenner</div><div class="role">Events</div></div>
</section>

<section class="sponsors">
  <div class="sec-title" style="top:40px"><div class="small">Our</div><div class="big">Sponsors</div></div>
  <div class="tier" style="top:140px"><div class="small">Sponsors</div><div class="big">Gold</div></div>
  <div class="logo-row" style="top:225px">
    <div class="sponsor">Norvia</div><div class="sponsor"><i></i>Mirabo</div><div class="sponsor">Cresta</div><div class="sponsor">Kelvar</div><div class="sponsor">Norvia</div>
  </div>
  <div class="tier" style="top:325px"><div class="small">Sponsors</div><div class="big">Silver</div></div>
  <div class="logo-row" style="top:410px">
    <div class="sponsor"><i></i>Orbelo</div><div class="sponsor">Swanta</div><div class="sponsor">Cresta</div><div class="sponsor">VRX</div><div class="sponsor">Cresta</div>
  </div>
  <div class="tier" style="top:510px"><div class="small">Sponsors</div><div class="big">Bronze</div></div>
  <div class="logo-row" style="top:595px">
    <div class="sponsor">Norvia</div><div class="sponsor">Corvela</div><div class="sponsor">Kelvar</div><div class="sponsor"><i></i>Orbelo</div><div class="sponsor">Mirabo</div>
  </div>
</section>

<footer class="site-footer">
  <div class="footer-photo" role="img" aria-label="Close-up of a golf club next to a ball on a tee"></div>
  <div class="f-col" style="left:615px;top:70px;width:240px">
    <h4>Our Location</h4>
    <div>VRX Putt 2016</div>
    <div>Tannweide Strasse 12, 3000 Bern</div>
    <div class="f-row"><svg width="12" height="12" viewBox="0 0 12 12"><path d="M3 1l2 3-1.5 1.5a7 7 0 0 0 3 3L8 7l3 2-1 2C5 11 1 7 1 2z" fill="#9bcb3c"/></svg>+41 31 555 01 20</div>
    <div class="f-row"><svg width="12" height="12" viewBox="0 0 12 12"><rect x="1" y="2.5" width="10" height="7" fill="none" stroke="#9bcb3c"/><path d="M1 2.5l5 4 5-4" fill="none" stroke="#9bcb3c"/></svg>hello@vrxputt.ch</div>
    <h4 style="margin-top:26px">More Info</h4>
    <div>Terms of Use</div><div>Privacy Policy</div><div>Sitemap</div>
  </div>
  <div class="f-col" style="left:885px;top:70px;width:240px">
    <h4>Quick Links</h4>
    <div>Welcome</div><div>Program</div><div>Information</div><div>Registration</div><div>Sponsors</div><div>Contact</div>
    <h4 style="margin-top:26px">Stay Connected</h4>
    <div class="social"><span></span><span></span><span></span><span></span></div>
  </div>
  <div class="copyright">© 2016 VRX Putt 2016. All rights reserved.</div>
</footer>

</body>
</html>
```